Naturopath Practitioner Card Design

I am a naturopath needing a design for a business card mainly to show that I am a naturopath and have some contact details to give to prospective clients. I am open minded about the design and what is on the second side of the card whether it just be some artwork or space for details, appointment times etc. Naturopathy is the practice of natural medicine that uses a holistic approach and incorporates herbal and nutritional medicine.

Industry/Entity Type

Business

Contact Information for Business Card

Tom Welby NaturopathBHSc (Naturopathy) Member PHRA 0492 815 306 tom.welby@mailbright.com www.tomwelbynaturopathy.com.au

Requirements
Nice to have
• Would prefer some kind of original pattern/art work/logo rather than an image, not fussed if its very simple/basic
• I am open to any colour but think I would prefer a more earthy sandy clay etc type style than the greens that are commonly associated with naturopathy.
Should not have
• Don't really want to have generic stock images on it

```html
<!DOCTYPE html>
<html lang="en">
<head>
<meta charset="utf-8">
<title>Tom Welby Naturopath – Business Card</title>
<link rel="stylesheet" href="https://fonts.googleapis.com/css2?family=Share+Tech&family=Share+Tech+Mono&display=swap">
<style>
  :root {
    --page-bg: #e4e1dc;
    --card-dark: #2f3236;
    --card-black: #1c1d1f;
    --brand-blue: #1e9ad8;
    --paper-white: #f2f2f2;
    --text-light: #ffffff;
    --text-ink: #23262a;
    --icon-dark: #2a2c2f;
  }
  * { box-sizing: border-box; margin: 0; padding: 0; }
  html, body { width: 1200px; height: 1000px; overflow: hidden; }
  body { background: var(--page-bg); position: relative; font-family: "Share Tech", sans-serif; }

  .card {
    position: absolute;
    width: 640px;
    height: 366px;
    background: var(--card-dark);
    overflow: hidden;
    box-shadow: 0 6px 18px rgba(0,0,0,0.18);
  }
  .card--details { left: 80px; top: 90px; }
  .card--front { left: 480px; top: 544px; }

  /* details side */
  .details__paper {
    position: absolute; left: 0; top: 130px; width: 150px; height: 180px;
    background: var(--paper-white);
  }
  .details__band {
    position: absolute; left: 110px; top: 110px; width: 530px; height: 130px;
    background: var(--brand-blue);
  }
  .details__mark {
    position: absolute; left: 28px; top: 40px;
    display: flex; align-items: center; gap: 8px;
    color: var(--text-light); font-size: 15px; letter-spacing: 0.5px;
  }
  .details__mark-square {
    width: 14px; height: 14px; border: 2px solid var(--brand-blue);
  }
  .contact-row {
    position: absolute; display: flex; align-items: flex-start; gap: 10px;
    font-family: "Share Tech Mono", monospace; color: var(--text-ink);
  }
  .contact-row--person { left: 300px; top: 126px; }
  .contact-row--email { left: 322px; top: 196px; align-items: center; }
  .contact-icon {
    width: 30px; height: 30px; border-radius: 50%;
    background: var(--icon-dark);
    display: flex; align-items: center; justify-content: center;
    color: var(--text-light); font-size: 15px; flex-shrink: 0;
    box-shadow: 0 1px 3px rgba(0,0,0,0.35);
  }
  .contact-name { font-size: 17px; line-height: 1.1; }
  .contact-meta { font-size: 12px; line-height: 1.3; }
  .contact-email { font-size: 13px; }

  /* front side */
  .front__band-left {
    position: absolute; left: 0; top: 178px; width: 360px; height: 108px;
    background: var(--brand-blue);
  }
  .front__band-right {
    position: absolute; left: 400px; top: 60px; width: 240px; height: 92px;
    background: var(--brand-blue);
  }
  .front__block {
    position: absolute; left: 300px; top: 80px; width: 160px; height: 190px;
    background: var(--card-black);
    display: flex; align-items: center; justify-content: center;
  }
  .front__mark {
    color: var(--text-light); font-size: 20px; text-align: center; line-height: 1.2;
    letter-spacing: 0.5px;
  }
  .company-name {
    position: absolute; left: 40px; top: 214px;
    color: var(--text-light); font-size: 30px; letter-spacing: 1px;
  }
  .company-slogan {
    position: absolute; left: 478px; top: 94px;
    color: var(--text-light); font-family: "Share Tech Mono", monospace; font-size: 13px;
  }
</style>
</head>
<body>

<section class="card card--details" aria-label="Business card, contact side">
  <div class="details__paper"></div>
  <div class="details__band"></div>
  <div class="details__mark"><span class="details__mark-square"></span>Tom Welby</div>

  <div class="contact-row contact-row--person">
    <span class="contact-icon">
      <svg width="14" height="14" viewBox="0 0 14 14" aria-hidden="true">
        <circle cx="7" cy="4.5" r="3" fill="#ffffff"/>
        <path d="M1.5 13c0-3 2.5-5 5.5-5s5.5 2 5.5 5z" fill="#ffffff"/>
      </svg>
    </span>
    <div>
      <p class="contact-name">Tom WelbyNaturopath</p>
      <p class="contact-meta">BHSc (Naturopathy)</p>
      <p class="contact-meta">Member PHRA0492 815</p>
    </div>
  </div>

  <div class="contact-row contact-row--email">
    <span class="contact-icon">@</span>
    <p class="contact-email">306tom.welby@mailbright.com</p>
  </div>
</section>

<section class="card card--front" aria-label="Business card, front side">
  <div class="front__band-left"></div>
  <div class="front__band-right"></div>
  <div class="front__block">
    <p class="front__mark">Tom<br>Welby</p>
  </div>
  <p class="company-name">COMPANY NAME</p>
  <p class="company-slogan">Company Slogan Here</p>
</section>

</body>
</html>
```